Social Media Post Quote #1 - Native American Organization

- SOLVANE - must be included
- Protect your community. Protect Your Elders. Stay Vaccinated. must be included
- Attached, company Logo, campaign logos and sample flu social media image. - our audience likes BRIGHT colors.
- Must include image from the United States, representing Land/Nature from one of the following regions, Plains and Woodlands, or Southwest, or Mountains, or Coast, or Pow-wow.
- must include quote “Don’t let the flu interfere with our gatherings.” – Anonymous Tribal Member
- One image will be provided twice - incorporating campaign logos - in some fashion

```html
<!DOCTYPE html>
<html lang="en">
<head>
<meta charset="utf-8">
<title>Solvane – Flu Gatherings Quote</title>
<link rel="stylesheet" href="https://fonts.googleapis.com/css2?family=Barlow:wght@400&family=Barlow+Condensed:wght@400;500;700&family=Barlow+Semi+Condensed:wght@400&display=swap">
<style>
  :root {
    --page: #ffffff;
    --sky-deep: #1f5fa8;
    --sky-light: #6f9bcc;
    --dusk-pink: #c98ea3;
    --rock-red: #c0564a;
    --sand: #d99273;
    --cream: #efe5dc;
    --quote-fill: rgba(196, 72, 96, 0.72);
    --white: #ffffff;
    --brown: #5a2e12;
    --brick: #b85a5a;
    --rose: #c0485f;
  }
  * { margin: 0; padding: 0; box-sizing: border-box; }
  html, body { width: 1200px; height: 496px; overflow: hidden; background: var(--page); }
  .canvas { position: relative; width: 1200px; height: 496px; }

  .post { position: absolute; top: 0; width: 495px; height: 496px; overflow: hidden; }
  .post--flu { left: 98px; }
  .post--combined { left: 599px; }

  .landscape {
    position: absolute; inset: 0;
    background: linear-gradient(180deg,
      var(--sky-deep) 0%, var(--sky-light) 28%, var(--dusk-pink) 42%,
      var(--rock-red) 56%, var(--sand) 68%, var(--cream) 82%, var(--cream) 100%);
  }

  .headline {
    position: absolute; top: 23px; left: 22px;
    font-family: "Barlow Semi Condensed", sans-serif; font-weight: 400;
    color: var(--white); text-transform: uppercase; white-space: nowrap;
    font-size: 18.5px; letter-spacing: 0.1px;
  }
  .post--combined .headline { top: 25px; font-size: 15.6px; }

  .quote-box {
    position: absolute; left: 74px; top: 135px; width: 345px; height: 176px;
    background: var(--quote-fill);
    border: 1.5px solid var(--white); border-top: none;
    text-align: center; color: var(--white);
  }
  .quote-box::before, .quote-box::after {
    content: ""; position: absolute; top: 0; height: 1.5px; width: 136px; background: var(--white);
  }
  .quote-box::before { left: -1.5px; }
  .quote-box::after { right: -1.5px; }

  .quote-mark {
    position: absolute; left: 50%; top: -36px; transform: translateX(-50%);
    font-family: "Barlow Condensed", sans-serif; font-weight: 700;
    font-size: 140px; line-height: 1; color: var(--white);
  }
  .quote-text {
    position: absolute; left: 0; right: 0; top: 30px;
    font-family: "Barlow Condensed", sans-serif; font-weight: 400;
    font-size: 45px; line-height: 35px; letter-spacing: -1.2px;
  }
  .quote-author {
    position: absolute; left: 0; right: 0; top: 149px;
    font-family: "Barlow", sans-serif; font-style: normal;
    font-size: 11.5px; letter-spacing: 5px;
  }

  .campaign-name {
    position: absolute; left: 25px; top: 388px; width: 247px; height: 57px;
    display: flex; align-items: center; justify-content: center;
    font-family: "Barlow Semi Condensed", sans-serif; font-weight: 400;
    font-size: 46px; letter-spacing: 1px; color: var(--brown);
  }

  .partner-name {
    position: absolute; left: 302px; top: 404px; width: 170px;
    font-family: "Barlow Condensed", sans-serif; font-weight: 500;
    font-size: 15px; line-height: 15px; color: var(--rose); text-transform: uppercase;
  }

  .tagline {
    position: absolute; left: 23px; top: 455px;
    font-family: "Barlow Semi Condensed", sans-serif; font-weight: 400;
    font-size: 16px; color: var(--brick); text-transform: uppercase; white-space: nowrap;
  }
</style>
</head>
<body>
<main class="canvas">
  <article class="post post--flu">
    <div class="landscape" role="img" aria-label="Southwest desert landscape with red sandstone buttes under a blue sky with pink clouds"></div>
    <p class="headline">Learn more about getting vaccinated against the flu</p>
    <blockquote class="quote-box">
      <span class="quote-mark">“</span>
      <p class="quote-text">Don’t let the flu<br>interfere with our<br>gatherings.</p>
      <cite class="quote-author">Anonymous Tribal Member</cite>
    </blockquote>
    <p class="campaign-name">Solvane</p>
    <p class="partner-name">Northwind<br>Elders Alliance</p>
    <p class="tagline">Protect your community. Protect your elders. Stay vaccinated.</p>
  </article>

  <article class="post post--combined">
    <div class="landscape" role="img" aria-label="Southwest desert landscape with red sandstone buttes under a blue sky with pink clouds"></div>
    <p class="headline">Learn more about getting vaccinated against COVID-19 &amp; the flu</p>
    <blockquote class="quote-box">
      <span class="quote-mark">“</span>
      <p class="quote-text">Don’t let the flu<br>interfere with our<br>gatherings.</p>
      <cite class="quote-author">Anonymous Tribal Member</cite>
    </blockquote>
    <p class="campaign-name">Solvane</p>
    <p class="partner-name">Northwind<br>Elders Alliance</p>
    <p class="tagline">Protect your community. Protect your elders. Stay vaccinated.</p>
  </article>
</main>
</body>
</html>
```